Evening of Discovery Annual Fundraising Dinner

I need a design for an invitation to our Evening of Discovery fundraising dinner.
The organization is called Halvern Joint Science Trust Foundation. (Find info at movewellfund.example)
Our organization tries to raise money to fund research into arthritis - all the different kinds of arthritis. We fund cutting edge research by giving grants to young scientists at different universities . I'm looking for an innovative design for the invitation to this event .
At this event we introduce our audience to to Scientists that we gave grants to in the previous year and tell them about the scientists who applied for grants this year. We also use the event to raise money towards these grants

Target Market(s)

Adults who suffer from Arthritis or who have relatives who suffer from arthritis and who want to learn more about the research being done to try to find a cure and who are willing to donate towards the cause

Industry/Entity Type

Foundation

Font styles to use
Sans Serif

Colors
ed2a32
0355a3

Requirements
Should not have
• We are NOT the Corlane Health Society we are a REsearch foundation .... Raising money for research .

```html
<!DOCTYPE html>
<html lang="en">
<head>
<meta charset="utf-8">
<title>Evening of Discovery – Fundraising Dinner Invitation</title>
<link rel="stylesheet" href="https://fonts.googleapis.com/css2?family=Montserrat:wght@300;400;700&family=Playball&family=Bebas+Neue&display=swap">
<style>
  :root {
    --brand-blue: #0355a3;
    --deep-blue: #0a3674;
    --mid-blue: #0b4f92;
    --teal: #3fb6cf;
    --teal-soft: #1c7fa8;
    --white: #ffffff;
    --ink: #2f3237;
    --brand-red: #ed2a32;
  }
  * { margin: 0; padding: 0; box-sizing: border-box; }
  html, body {
    width: 1200px; height: 1200px; overflow: hidden;
    background: var(--white);
  }
  .canvas { position: relative; width: 1200px; height: 1200px; background: var(--white); }

  .invitation-card {
    position: absolute; left: 32px; top: 38px; width: 1136px; height: 946px;
    overflow: hidden;
    background:
      radial-gradient(ellipse 70% 55% at 45% 45%, rgba(30,110,180,0.55), rgba(30,110,180,0) 70%),
      linear-gradient(180deg, #05599c 0%, var(--mid-blue) 45%, var(--deep-blue) 100%);
    color: var(--white);
  }

  .network-art { position: absolute; right: 0; bottom: 0; width: 1136px; height: 946px; }

  .event-title {
    position: absolute; left: 0; width: 952px; top: 104px; text-align: center;
    font-family: "Playball", cursive; font-weight: 400; font-size: 94px; line-height: 1;
  }
  .event-subtitle {
    position: absolute; left: 0; width: 952px; top: 232px; text-align: center;
    font-family: "Montserrat", sans-serif; font-weight: 700; font-size: 40px; letter-spacing: 0.5px;
  }
  .invite-line {
    position: absolute; left: 60px; width: 952px; top: 390px; text-align: center;
    font-family: "Playball", cursive; font-size: 136px; line-height: 1;
  }

  .event-details {
    position: absolute; left: 67px; top: 626px;
    font-family: "Montserrat", sans-serif; font-size: 26px; line-height: 35px;
  }
  .event-details .label { font-weight: 700; }
  .event-details .info { font-weight: 300; letter-spacing: 0.3px; }
  .event-details .venue { margin-top: 48px; }

  .org-mark {
    position: absolute; left: 900px; top: 38px; width: 200px; height: 228px;
    background: var(--white);
    display: flex; align-items: center; justify-content: center;
  }
  .org-mark .mark-inner {
    width: 164px; height: 176px; background: var(--ink);
    display: flex; flex-direction: column; align-items: center; justify-content: center; gap: 14px;
    padding: 0 10px;
  }
  .org-mark .mark-dot { width: 52px; height: 52px; border-radius: 50%; background: var(--brand-blue); }
  .org-mark .mark-name {
    font-family: "Montserrat", sans-serif; font-weight: 700; font-size: 14px; line-height: 18px;
    color: var(--white); text-align: center; text-transform: uppercase;
  }

  .version-label {
    position: absolute; right: 30px; top: 1046px;
    font-family: "Bebas Neue", sans-serif; font-size: 80px; line-height: 1; color: var(--ink);
    letter-spacing: 1px;
  }
</style>
</head>
<body>
<div class="canvas">
  <section class="invitation-card">
    <svg class="network-art" viewBox="0 0 1136 946" role="img" aria-label="Abstract network of connected glowing points and teal facets, suggesting scientific discovery">
      <defs>
        <linearGradient id="facetGlow" x1="1" y1="1" x2="0.3" y2="0.3">
          <stop offset="0" stop-color="#3fb6cf" stop-opacity="0.75"/>
          <stop offset="0.6" stop-color="#1c7fa8" stop-opacity="0.4"/>
          <stop offset="1" stop-color="#1c7fa8" stop-opacity="0"/>
        </linearGradient>
      </defs>
      <polygon points="1136,350 978,432 890,600 770,740 610,860 400,946 1136,946" fill="url(#facetGlow)"/>
    </svg>

    <h1 class="event-title">Evening of Discovery</h1>
    <p class="event-subtitle">FUNDRAISING DINNER</p>
    <p class="invite-line">You are invited!</p>

    <div class="event-details">
      <p class="label">April 5, 2017</p>
      <p class="info">Start time is 6:00pm</p>
      <div class="venue">
        <p class="label">Harborline Club Alder Bay</p>
        <p class="info">418 Meridian Plaza Drive, Garden Level</p>
        <p class="info">Alder Bay, CA 92000</p>
      </div>
    </div>

    <div class="org-mark">
      <div class="mark-inner">
        <span class="mark-dot"></span>
        <span class="mark-name">Halvern Joint Science Trust Foundation</span>
      </div>
    </div>
  </section>

  <p class="version-label">VERSION 01</p>
</div>
</body>
</html>
```